Business card for communications

Need a business card for my consulting business - I work with not for profits, start ups and social enterprises on their media, communications campaigns.

Please see my website for colours, images and fonts www.morvenquillet.example

Morven Quillet
Communications & Campaign strategist
Sydney - Melbourne
M: 0498 317 250
E: morven@morvenquillet.example
S: morvenquillet
W: morvenquillet.example
T: @morvenquillet

(above is info only and can be presented any way e.g. should not have to be M for mobile - it should be an icon)
Updates

Dear designers I have updated the brief and uploaded high res images from my website for you to use. The designs so far with the use of images and icons are much better so far. Thank you I look forward to receiving your revised designs. Morven Quillet

Industry/Entity Type

Communications

Font styles to use
Sans Serif

Requirements
Must have
• Icons for contact details
Images from the website www.morvenquillet.example
Nice to have
• Images - attached

```html
<!DOCTYPE html>
<html lang="en">
<head>
<meta charset="utf-8">
<title>Morven Quillet — Business Card</title>
<link rel="stylesheet" href="https://fonts.googleapis.com/css2?family=Lato:wght@300;400&display=swap">
<style>
  :root {
    --stage: #e9e6e0;
    --card-yellow: #f5e10f;
    --card-yellow-deep: #efd20a;
    --ink: #1c1a1b;
    --ink-soft: #3a3839;
    --paper-white: #ffffff;
    --name-light: #fdfbe6;
  }
  * { box-sizing: border-box; margin: 0; padding: 0; }
  html, body {
    width: 1200px;
    height: 1023px;
    overflow: hidden;
    background: var(--stage);
    font-family: "Lato", sans-serif;
  }
  .card {
    position: absolute;
    left: 150px;
    top: 251px;
    width: 900px;
    height: 520px;
    overflow: hidden;
    box-shadow: 0 18px 40px rgba(0,0,0,0.22);
  }
  .card-shapes {
    position: absolute;
    inset: 0;
    width: 100%;
    height: 100%;
  }
  .brand-name {
    position: absolute;
    left: 70px;
    top: 300px;
    color: var(--paper-white);
    font-weight: 300;
    font-size: 40px;
    letter-spacing: 1px;
    white-space: nowrap;
  }
  .identity {
    position: absolute;
    left: 430px;
    top: 72px;
    white-space: nowrap;
  }
  .identity-name {
    color: var(--name-light);
    font-weight: 400;
    font-size: 30px;
    line-height: 1.1;
  }
  .identity-role {
    color: var(--ink-soft);
    font-weight: 300;
    font-size: 21px;
    line-height: 1.3;
  }
  .divider {
    position: absolute;
    left: 468px;
    top: 170px;
    width: 320px;
    height: 6px;
    background: linear-gradient(90deg, var(--ink), var(--ink-soft));
  }
  .contacts {
    position: absolute;
    left: 440px;
    top: 240px;
    display: grid;
    grid-template-columns: 190px 240px;
    row-gap: 24px;
    column-gap: 10px;
  }
  .contact {
    display: flex;
    align-items: center;
    gap: 10px;
    color: var(--ink);
    font-weight: 400;
    font-size: 18px;
    white-space: nowrap;
  }
  .contact-icon {
    width: 22px;
    height: 22px;
    flex: none;
  }
  .mark-circle {
    width: 22px;
    height: 22px;
    border-radius: 50%;
    background: var(--ink-soft);
    flex: none;
  }
  .mark-square {
    width: 20px;
    height: 20px;
    background: var(--ink-soft);
    flex: none;
  }
</style>
</head>
<body>
  <div class="card">
    <svg class="card-shapes" viewBox="0 0 900 520" aria-hidden="true">
      <defs>
        <linearGradient id="yellowFill" x1="0" y1="0" x2="1" y2="1">
          <stop offset="0" stop-color="#f7e81a"/>
          <stop offset="1" stop-color="#efd20a"/>
        </linearGradient>
        <linearGradient id="inkFill" x1="0" y1="0" x2="1" y2="1">
          <stop offset="0" stop-color="#2a2829"/>
          <stop offset="0.55" stop-color="#4a4849"/>
          <stop offset="1" stop-color="#1c1a1b"/>
        </linearGradient>
      </defs>
      <rect width="900" height="520" fill="url(#yellowFill)"/>
      <path d="M0,30 C260,40 470,180 540,440 L900,440 L900,520 L0,520 Z" fill="url(#inkFill)"/>
      <path d="M0,30 C260,40 470,180 540,440" fill="none" stroke="#ffffff" stroke-width="9"/>
      <rect x="0" y="440" width="900" height="80" fill="#1c1a1b"/>
    </svg>

    <div class="brand-name">Morven Quillet</div>

    <div class="identity">
      <p class="identity-name">Morven Quillet</p>
      <p class="identity-role">Communications &amp; Campaign strategist</p>
    </div>

    <div class="divider"></div>

    <div class="contacts">
      <div class="contact"><span class="mark-circle"></span>morvenquillet</div>
      <div class="contact"><span class="mark-square"></span>@morvenquillet</div>
      <div class="contact">
        <svg class="contact-icon" viewBox="0 0 24 24" aria-hidden="true">
          <path d="M3 9c0-3 4-5 9-5s9 2 9 5l-4 1-1-3H8L7 10Z" fill="#3a3839"/>
          <rect x="5" y="11" width="14" height="9" rx="2" fill="#3a3839"/>
          <circle cx="12" cy="15.5" r="2.5" fill="#f5e10f"/>
        </svg>
        0498 317 250
      </div>
      <div class="contact">
        <svg class="contact-icon" viewBox="0 0 24 24" aria-hidden="true">
          <g fill="none" stroke="#3a3839" stroke-width="1.6">
            <circle cx="12" cy="12" r="9.5"/>
            <ellipse cx="12" cy="12" rx="4" ry="9.5"/>
            <line x1="2.5" y1="12" x2="21.5" y2="12"/>
            <line x1="4" y1="7" x2="20" y2="7"/>
            <line x1="4" y1="17" x2="20" y2="17"/>
          </g>
        </svg>
        morvenquillet.example
      </div>
    </div>
  </div>
</body>
</html>
```